Sunny Hour Spirits Gin label

I’m looking for a gin label that as the title says it should be a bright and fun filled label for . The gin will have four seasons so each season will have a different label starting with a summer gin. It should be fright and cooler full happy and fun The name of the Gin is Sunny Hour Spirits Gin it should be bright and jump off the shelf.

Target Market(s)

Gin buyers

Font styles to use
Decorative
Script

Colors

Designer to choose colors to be used in the design.

Requirements
Must have
• Bright colours interesting eye catching

```html
<!DOCTYPE html>
<html lang="en">
<head>
<meta charset="utf-8">
<title>Sunny Hour Spirits Gin – Summer Edition Label</title>
<link rel="stylesheet" href="https://fonts.googleapis.com/css2?family=Fredoka:wght@500;600;700&display=swap">
<style>
  :root {
    --label-gold: #f7ae00;
    --backdrop: #ffffff;
  }
  html, body {
    margin: 0;
    padding: 0;
    width: 713px;
    height: 1200px;
    overflow: hidden;
    background: var(--backdrop);
  }
  .label {
    display: block;
    width: 713px;
    height: 1200px;
  }
  .label-ink-line {
    fill: none;
    stroke: var(--label-gold);
    stroke-linecap: round;
    stroke-linejoin: round;
  }
  .frame { stroke-width: 4; }
  .pillar-line { stroke-width: 3; }
  .edition-box { stroke-width: 4; fill: var(--backdrop); }
  .label-text {
    fill: var(--label-gold);
    font-family: "Fredoka", sans-serif;
    text-anchor: middle;
  }
  .brand-arc { font-size: 25px; font-weight: 700; letter-spacing: 1px; }
  .gin-word { font-size: 92px; font-weight: 700; }
  .spec { font-size: 19px; font-weight: 600; letter-spacing: 1px; }
  .edition { font-size: 24px; font-weight: 600; letter-spacing: 1px; }
  .sunburst-area { fill: url(#sunburst-tone); }
  .palm-scene { fill: url(#palm-tone); }
</style>
</head>
<body>
<svg class="label" viewBox="232 508 406 683" xmlns="http://www.w3.org/2000/svg">
  <defs>
    <radialGradient id="sunburst-tone" cx="0.5" cy="1" r="0.9">
      <stop offset="0" stop-color="var(--label-gold)" stop-opacity="0.55"/>
      <stop offset="1" stop-color="var(--label-gold)" stop-opacity="0.12"/>
    </radialGradient>
    <linearGradient id="palm-tone" x1="0" y1="0" x2="0" y2="1">
      <stop offset="0" stop-color="var(--label-gold)" stop-opacity="0.25"/>
      <stop offset="1" stop-color="var(--label-gold)" stop-opacity="0.6"/>
    </linearGradient>
    <path id="brand-arc-path" d="M318 805 C318 640 552 640 552 805"/>
  </defs>

  <!-- sun rays above the arch -->
  <path class="sunburst-area"
        d="M285 628 L340 530 L530 530 L585 628 C540 600 330 600 285 628 Z"
        role="img" aria-label="Hand-drawn sun rays fanning out above the arch"/>

  <!-- arched label frame -->
  <path class="label-ink-line frame"
        d="M270 682 Q262 682 262 692 L262 1172 Q262 1182 272 1182 L602 1182 Q612 1182 612 1172 L612 692 Q612 682 604 682 L585 682 Q568 682 560 668 C528 620 342 620 310 668 Q302 682 285 682 Z"/>

  <!-- brand name on the arch -->
  <text class="label-text brand-arc">
    <textPath href="#brand-arc-path" startOffset="50%">SUNNY HOUR SPIRITS</textPath>
  </text>

  <!-- stacked product word -->
  <text class="label-text gin-word">
    <tspan x="434" y="815">G</tspan>
    <tspan x="434" y="903">I</tspan>
    <tspan x="434" y="993">N</tspan>
  </text>

  <!-- pillar lines -->
  <g class="label-ink-line pillar-line">
    <line x1="303" y1="828" x2="303" y2="930"/>
    <line x1="313" y1="828" x2="313" y2="930"/>
    <line x1="323" y1="828" x2="323" y2="930"/>
    <line x1="333" y1="828" x2="333" y2="930"/>
    <line x1="538" y1="828" x2="538" y2="930"/>
    <line x1="548" y1="828" x2="548" y2="930"/>
    <line x1="558" y1="828" x2="558" y2="930"/>
    <line x1="568" y1="828" x2="568" y2="930"/>
  </g>

  <!-- strength and volume -->
  <text class="label-text spec">
    <tspan x="328" y="964">40%</tspan>
    <tspan x="328" y="986">VOL.</tspan>
  </text>
  <text class="label-text spec">
    <tspan x="548" y="964">750</tspan>
    <tspan x="548" y="986">ml</tspan>
  </text>

  <!-- beach scene with palm trees -->
  <rect class="palm-scene" x="298" y="1015" width="62" height="122" rx="6"
        role="img" aria-label="Small drawing of a palm tree with seagulls on a beach"/>
  <rect class="palm-scene" x="505" y="1000" width="86" height="137" rx="6"
        role="img" aria-label="Small drawing of two palm trees on a beach"/>

  <!-- edition plaque -->
  <rect class="label-ink-line edition-box" x="347" y="1040" width="174" height="94" rx="6"/>
  <text class="label-text edition">
    <tspan x="434" y="1081">SUMMER</tspan>
    <tspan x="434" y="1111">EDITION</tspan>
  </text>
</svg>
</body>
</html>
```